Brookvale Insurance Services - Insurance Agency Wesbite

I need a website for my insurance agency called Brookvale Insurance Services. I have attached my company logo. You can use the colors from the copy logo to create the website color scheme. I need a Request A Quote section.
Business Address: 7816 Marlowe Ave Unit D, Studio City Ca 91627
Business Phone: (818) 555-0193
I would need the following drop downs on the main page:

1st drop down:
Business Insurance
⁃ Commercial Auto
⁃ Employment Practice Liability Insurance
⁃ General Liability Insurance
⁃ Professional Liability Insurance
⁃ Property Insurance
⁃ Workers Compensation Insurance

2nd drop down:
Industries We Serve
- Construction
- Janitorial
- Landscapers
- Trucking
- ParcelRun Independent Service Providers (ISP)
Healthcare Industry
- Community Care Facilities
- Home Health Agencies
- Hospice
- Nursing Homes

3rd drop down:
Risk Management
- Claims Management
- Compliance & Risk Management

4th drop down
Request a quote

5th drop down
About Us

6th drop down
Contact US

Target Market(s)

Potential clients

Industry/Entity Type

Business Insurance

Coding

Coded - Design and coding required

Number of Pages Required

5+ page

Colors
0054AA
0677BA
7BADD7
CADEEF
E8F1F8
00AB8E
00BBA5
67D7C9
C6EFE9
E9F9F6

Requirements
Must have
• Home Business Insurance - Commercial Auto - Employment Practice Liability Insurance - General Liability Insurance - Professional Liability Insurance - Property Insurance - Workers Compensation Insurance Industries We Serve - Construction - Janitorial - Landscapers - Manufacturing Companies - Restaurants - Towing - Trucking Healthcare Industry - Community Care Facilities - Home Health Agencies - Hospice - Nursing Homes - Risk Management - Claims Management - Compliance & Risk Management Request a Quote About Us Contact Us

```html
<!DOCTYPE html>
<html lang="en">
<head>
<meta charset="utf-8">
<title>Brookvale Insurance Services</title>
<link href="https://fonts.googleapis.com/css2?family=Roboto:wght@400;500;700&display=swap" rel="stylesheet">
<style>
:root{
  --navy:#0b2b80;
  --navy-dark:#030d30;
  --green:#079a34;
  --hero-bg:#e3e8ef;
  --page:#f7fcf9;
  --ink:#111827;
  --muted:#9aa0a8;
  --white:#ffffff;
}
*{box-sizing:border-box;margin:0;padding:0}
html,body{width:1200px;height:3680px;overflow:hidden}
body{position:relative;font-family:'Roboto',sans-serif;color:var(--ink);background:var(--page)}
.abs{position:absolute}
.photo{position:absolute}
.btn{position:absolute;background:var(--navy);color:var(--white);font-size:16px;display:flex;align-items:center;justify-content:center}
.brand{font-weight:700;color:var(--navy);font-size:24px;letter-spacing:.5px;display:flex;align-items:center;gap:10px}
.brand .dot{width:14px;height:14px;background:var(--green)}
/* header */
.topbar{left:0;top:0;width:1200px;height:106px;background:var(--white)}
.contact-item{display:flex;align-items:center;gap:16px;font-size:13px;line-height:22px}
.contact-item b{font-weight:700}
.nav{left:0;top:106px;width:1200px;height:70px;background:var(--navy);display:flex;justify-content:center;align-items:center;gap:28px;color:var(--white);font-size:13px}
.nav span{display:flex;align-items:center;gap:8px}
/* hero */
.hero-bg{left:0;top:176px;width:854px;height:521px;background:var(--hero-bg)}
.hero-green{left:854px;top:176px;width:346px;height:521px;background:var(--green)}
h1{position:absolute;left:83px;top:296px;font-size:40px;font-weight:500;line-height:47px;width:560px}
.hero-text{left:83px;top:418px;width:500px;font-size:16px;line-height:19px}
/* about */
.frame{left:60px;top:846px;width:416px;height:547px;border:1px solid var(--green)}
h2{position:absolute;font-weight:500}
.about-text{left:559px;top:1054px;width:545px;font-size:16.5px;line-height:23.5px}
.ticks{left:559px;top:1172px;list-style:none;font-size:16.5px}
.ticks li{display:flex;align-items:center;gap:10px;height:36.5px}
.stat{position:absolute;top:1476px;width:300px;text-align:center}
.stat .num{font-size:54px;font-weight:700;color:var(--green);line-height:64px}
.stat .num small{font-size:30px}
.stat .lbl{font-size:16.5px;margin-top:12px}
/* services */
.tab{position:absolute;top:1799px;width:100px;height:100px;border:1px solid #b9bec6;border-top:1px solid #b9bec6;display:flex;flex-direction:column;align-items:center;justify-content:flex-start;padding-top:20px}
.tab .label{position:absolute;top:52px;background:var(--page);padding:0 4px;white-space:nowrap;font-size:16px;color:var(--muted)}
.tab.active{border-color:var(--navy)}
.tab.active .label{color:var(--navy)}
.card{position:absolute;width:336px;height:149px;background:var(--white);box-shadow:0 2px 12px rgba(0,0,0,.1);padding:20px 13px}
.card h3{font-size:16px;font-weight:700;margin-bottom:13px}
.card p{font-size:12.5px;line-height:15.5px}
.card a{display:inline-block;margin-top:6px;font-size:12.5px;color:var(--navy);text-decoration:underline}
/* quote */
.qtabs{left:473px;top:2636px;width:644px;height:53px;border-bottom:2px solid var(--navy);display:flex}
.qtabs div{flex:1;display:flex;align-items:center;gap:16px;padding-left:16px;font-size:13px;line-height:15px}
.qtabs .on{background:var(--navy);color:var(--white)}
.field{position:absolute;left:499px;width:591px;height:52px;border:1px solid var(--navy);background:var(--page);font-size:16px;color:#6b7280;display:flex;align-items:center;padding-left:16px}
/* contact */
.contact-band{left:0;top:3141px;width:1200px;height:209px;background:var(--navy);color:var(--white)}
.contact-row{position:absolute;top:3258px;left:0;width:1200px;display:flex;justify-content:center;gap:56px;color:var(--white);font-size:17px}
.contact-row span{display:flex;align-items:center;gap:18px}
/* footer */
.footer{left:0;top:3350px;width:1200px;height:330px;background:var(--navy-dark);color:var(--white)}
.fcol{position:absolute;top:3404px;font-size:13px;line-height:17px}
.fcol h4{font-size:13px;font-weight:700;margin-bottom:12px}
.fcol p{margin-bottom:6px}
.fcol u{text-decoration:underline}
</style>
</head>
<body>

<header class="abs topbar">
  <div class="abs brand" style="left:83px;top:38px">Brookvale<span class="dot"></span></div>
  <div class="abs contact-item" style="left:725px;top:32px">
    <svg width="34" height="34" viewBox="0 0 24 24"><path fill="#0b2b80" d="M6.6 10.8a15.2 15.2 0 0 0 6.6 6.6l2.2-2.2a1 1 0 0 1 1-.25 11.4 11.4 0 0 0 3.6.57 1 1 0 0 1 1 1V20a1 1 0 0 1-1 1A17 17 0 0 1 3 4a1 1 0 0 1 1-1h3.5a1 1 0 0 1 1 1c0 1.25.2 2.45.57 3.57a1 1 0 0 1-.25 1z"/></svg>
    <div><b>Phone</b><br>(818) 555-0193</div>
  </div>
  <div class="abs contact-item" style="left:924px;top:32px">
    <svg width="36" height="28" viewBox="0 0 36 28"><rect width="36" height="28" rx="3" fill="#0b2b80"/><path d="M4 5l14 11L32 5" stroke="#fff" stroke-width="3" fill="none"/></svg>
    <div><b>7816 Marlowe Ave Unit D,</b><br>Studio City Ca 91627</div>
  </div>
</header>

<nav class="abs nav">
  <span>Bussiness Insurance <svg width="10" height="6"><path d="M1 1l4 4 4-4" stroke="#fff" fill="none" stroke-width="1.5"/></svg></span>
  <span>Industries We Serve <svg width="10" height="6"><path d="M1 1l4 4 4-4" stroke="#fff" fill="none" stroke-width="1.5"/></svg></span>
  <span>Health Insurance <svg width="10" height="6"><path d="M1 1l4 4 4-4" stroke="#fff" fill="none" stroke-width="1.5"/></svg></span>
  <span>Risk Management <svg width="10" height="6"><path d="M1 1l4 4 4-4" stroke="#fff" fill="none" stroke-width="1.5"/></svg></span>
  <span>Request A Quote</span>
  <span>About</span>
  <span>Contact Us</span>
</nav>

<section>
  <div class="abs hero-bg"></div>
  <div class="abs hero-green"></div>
  <h1>Tailored Insurance for Your Every Life Chapter.</h1>
  <p class="abs hero-text">At the heart of our insurance services is a commitment to security, offering personalized coverage that evolves with your changing needs.</p>
  <div class="btn" style="left:83px;top:503px;width:178px;height:51px">Request A Quote</div>
  <div class="photo" role="img" aria-label="Agent shaking hands with a smiling couple in an office" style="left:694px;top:244px;width:423px;height:499px;background:linear-gradient(160deg,#c9c6c0,#8a8e95 55%,#3c3f48)"></div>
</section>

<section>
  <div class="abs frame"></div>
  <div class="photo" role="img" aria-label="Insurance advisor reviewing documents with an elderly client" style="left:83px;top:870px;width:423px;height:564px;background:linear-gradient(150deg,#b9b4aa,#7c7f84 50%,#3a3d44)"></div>
  <h2 style="left:559px;top:955px;font-size:30px;line-height:35px;width:520px">Crafting a Protected Path for Your Journey</h2>
  <p class="abs about-text">Experience the difference of insurance with a human touch. Our company is dedicated to understanding your unique needs, offering responsive service, and delivering peace of mind through thoughtful and comprehensive coverage.</p>
  <ul class="abs ticks">
    <li><svg width="16" height="12"><path d="M1 6l4 4 10-9" stroke="#0b2b80" fill="none" stroke-width="1.6"/></svg>Financial Security</li>
    <li><svg width="16" height="12"><path d="M1 6l4 4 10-9" stroke="#0b2b80" fill="none" stroke-width="1.6"/></svg>Tailored Coverage</li>
    <li><svg width="16" height="12"><path d="M1 6l4 4 10-9" stroke="#0b2b80" fill="none" stroke-width="1.6"/></svg>Asset Protection</li>
  </ul>
  <div class="btn" style="left:559px;top:1296px;width:138px;height:51px">Learn more</div>

  <div class="stat" style="left:109px"><div class="num">123</div><div class="lbl">Projects Completed</div></div>
  <div class="stat" style="left:449px"><div class="num">$4.5 <small>billion</small></div><div class="lbl">Insurance Payouts</div></div>
  <div class="stat" style="left:790px"><div class="num">100%</div><div class="lbl">Claim Success Rate</div></div>
</section>

<section>
  <h2 style="left:0;width:1200px;text-align:center;top:1743px;font-size:30px">Wide Range of Tailored Insurance Services</h2>
  <div class="tab active" style="left:274px"><svg width="26" height="22" viewBox="0 0 26 22"><rect x="1" y="5" width="24" height="16" rx="2" fill="#0b2b80"/><rect x="9" y="1" width="8" height="5" fill="none" stroke="#0b2b80" stroke-width="2"/><rect x="11" y="11" width="4" height="3" fill="#fff"/></svg><span class="label">Business Insurance</span></div>
  <div class="tab" style="left:457px"><svg width="28" height="24" viewBox="0 0 28 24"><path d="M2 23V2h14v21M16 8h10v15M1 23h26" stroke="#9aa0a8" fill="none" stroke-width="1.5"/><path d="M6 6h2M10 6h2M6 11h2M10 11h2M6 16h2M10 16h2M20 12h2M20 17h2" stroke="#9aa0a8" stroke-width="2"/></svg><span class="label">Industries</span></div>
  <div class="tab" style="left:641px"><svg width="28" height="26" viewBox="0 0 28 26"><path d="M5 25V4h18v21M1 25h26M12 25v-5h4v5M14 7v6M11 10h6" stroke="#9aa0a8" fill="none" stroke-width="1.5"/></svg><span class="label">Healthcare Industry</span></div>
  <div class="tab" style="left:824px"><svg width="22" height="26" viewBox="0 0 22 26"><path d="M2 1h12l6 6v18H2zM14 1v6h6M6 13h10M6 17h10M6 21h7" stroke="#9aa0a8" fill="none" stroke-width="1.5"/></svg><span class="label">Risk Management</span></div>

  <div class="card" style="left:83px;top:1993px"><h3>Commercial Auto</h3><p>Lorem ipsum dolor sit amet consectetur. Id pretium eget nunc magna sagittis lacus dui tortor. Orci semper integer nec ut nisi elit augue. Nunc egestas.</p><a>Learn More</a> <span style="font-size:12px;color:#0b2b80">&nbsp;→</span></div>
  <div class="card" style="left:439px;top:1993px"><h3>Employment Practice Liability Insurance</h3><p>Lorem ipsum dolor sit amet consectetur. Id pretium eget nunc magna sagittis lacus dui tortor. Orci semper integer nec ut nisi elit augue. Nunc egestas.</p><a>Learn More</a> <span style="font-size:12px;color:#0b2b80">&nbsp;→</span></div>
  <div class="card" style="left:83px;top:2161px"><h3>General Liability Insurance</h3><p>Lorem ipsum dolor sit amet consectetur. Id pretium eget nunc magna sagittis lacus dui tortor. Orci semper integer nec ut nisi elit augue. Nunc egestas.</p><a>Learn More</a> <span style="font-size:12px;color:#0b2b80">&nbsp;→</span></div>
  <div class="card" style="left:439px;top:2161px"><h3>Professional Liability Insurance</h3><p>Lorem ipsum dolor sit amet consectetur. Id pretium eget nunc magna sagittis lacus dui tortor. Orci semper integer nec ut nisi elit augue. Nunc egestas.</p><a>Learn More</a> <span style="font-size:12px;color:#0b2b80">&nbsp;→</span></div>
  <div class="abs" style="left:733px;top:2337px;font-size:15px;color:var(--navy)"><u style="font-weight:700">1</u>&nbsp;&nbsp;&nbsp;&nbsp;<span style="color:#6b7280">2</span></div>

  <div class="abs" style="left:809px;top:2020px;width:352px;height:309px;background:var(--green)"></div>
  <div class="photo" role="img" aria-label="Two colleagues reviewing a contract on a desk" style="left:824px;top:1926px;width:293px;height:498px;background:linear-gradient(170deg,#d9d7d3,#9a9691 55%,#4a4745)"></div>
</section>

<section>
  <div class="abs" style="left:0;top:2550px;width:376px;height:107px;background:var(--green)"></div>
  <div class="photo" role="img" aria-label="Smiling family with two young children at home" style="left:83px;top:2604px;width:336px;height:413px;background:linear-gradient(160deg,#d8d5d0,#a48f86 50%,#5a4440)"></div>
  <h2 style="left:473px;top:2582px;font-size:30px;font-weight:700">Get A Quote To Get Started!</h2>
  <div class="abs qtabs">
    <div class="on"><svg width="20" height="17" viewBox="0 0 26 22"><rect x="1" y="5" width="24" height="16" rx="2" fill="#fff"/><rect x="9" y="1" width="8" height="5" fill="none" stroke="#fff" stroke-width="2"/></svg>Business<br>Insurance</div>
    <div><svg width="22" height="19" viewBox="0 0 28 24"><path d="M2 23V2h14v21M16 8h10v15M1 23h26" stroke="#0b2b80" fill="none" stroke-width="2"/></svg>Industries</div>
    <div><svg width="22" height="22" viewBox="0 0 28 26"><path d="M5 25V4h18v21M1 25h26M14 7v6M11 10h6" stroke="#0b2b80" fill="none" stroke-width="2"/></svg>Healthcare<br>Industry</div>
    <div><svg width="17" height="21" viewBox="0 0 22 26"><path d="M2 1h12l6 6v18H2zM6 13h10M6 17h10" stroke="#0b2b80" fill="none" stroke-width="2"/></svg>Risk<br>Management</div>
  </div>
  <div class="field" style="top:2717px">Full name</div>
  <div class="field" style="top:2783px">Email</div>
  <div class="field" style="top:2849px;color:var(--ink);justify-content:space-between;padding-right:20px">Select insurance type <svg width="10" height="6"><path d="M1 1l4 4 4-4" stroke="#111" fill="none" stroke-width="1.5"/></svg></div>
  <div class="btn" style="left:499px;top:2927px;width:181px;height:53px">Get A Quote Now</div>
</section>

<section class="abs contact-band">
  <h2 style="left:0;width:1200px;text-align:center;top:54px;font-size:30px;font-weight:700">Contact Us</h2>
</section>
<div class="contact-row">
  <span><svg width="24" height="32" viewBox="0 0 24 32"><path d="M12 0a12 12 0 0 0-12 12c0 9 12 20 12 20s12-11 12-20A12 12 0 0 0 12 0z" fill="#fff"/><circle cx="12" cy="12" r="4.5" fill="#0b2b80"/></svg>7816 Marlowe Ave Unit D, Studio City Ca 91627</span>
  <span><svg width="32" height="32" viewBox="0 0 24 24"><path fill="#fff" d="M6.6 10.8a15.2 15.2 0 0 0 6.6 6.6l2.2-2.2a1 1 0 0 1 1-.25 11.4 11.4 0 0 0 3.6.57 1 1 0 0 1 1 1V20a1 1 0 0 1-1 1A17 17 0 0 1 3 4a1 1 0 0 1 1-1h3.5a1 1 0 0 1 1 1c0 1.25.2 2.45.57 3.57a1 1 0 0 1-.25 1z"/></svg>(818) 555-0193</span>
  <span><svg width="34" height="26" viewBox="0 0 36 28"><rect width="36" height="28" rx="3" fill="#fff"/><path d="M4 5l14 11L32 5" stroke="#0b2b80" stroke-width="3" fill="none"/></svg>hello@brookvaleins.com</span>
</div>

<footer class="abs footer">
  <div class="abs brand" style="left:83px;top:62px;color:var(--navy)">Brookvale<span class="dot"></span></div>
  <div class="abs" style="left:83px;top:150px;width:249px;border-bottom:1px solid #8b93a8;padding:0 13px 8px;font-size:13px;color:#9aa3b8">enter email address</div>
  <div class="abs" style="left:83px;top:190px;width:78px;height:30px;background:var(--green);font-size:12px;display:flex;align-items:center;justify-content:center">Subscribe</div>
</footer>
<div class="fcol" style="left:399px;color:#fff;width:190px">
  <h4>Business Insurance</h4>
  <p>Commercial Auto</p><p><u>Employment Practice Liability Insurance</u></p><p>General Liability Insurance</p><p>Professional Liability Insurance</p><p>Property Insurance</p><p>Workers Compensation Insurance</p>
</div>
<div class="fcol" style="left:660px;color:#fff">
  <h4>Industries</h4>
  <p>Construction</p><p><u>Janitorial</u></p><p>Landscapers</p><p>Manufacturing Companies</p><p>Restaurants</p><p>Towing</p><p>Trucking</p>
</div>
<div class="fcol" style="left:922px;color:#fff">
  <h4>Healthcare Industry</h4>
  <p>Community Care Facilities</p><p><u>Home Health Agencies</u></p><p>Hospice</p><p>Nursing Homes</p>
  <h4 style="margin-top:30px">Risk Management</h4>
  <p>Claims Management</p><p><u>Compliance &amp; Risk<br>Management</u></p>
</div>

</body>
</html>
```